Concierge Dental / Medical Supply Ordering Business - Sleek, Efficient, Professional, Elite

www.brimleyandfoxcare.example - example website.

We are a concierge supply ordering business for medical and dental that provide DSO price savings on supplies while maintaining business autonomy and independence.

We want a very simple website that looks very professional says what we do and gives a very simple method to contact us & sign up as above.

Target Market(s)

Independent Dental and Medical Practices

Industry/Entity Type

Dental and Medical - healthcare

Coding

Coded - Design and coding required

Number of Pages Required

3 page

Font styles to use
Sans Serif

Colors
0054AA
0677BA
7BADD7
CADEEF
E8F1F8

Requirements
Must have
• Simple contact page, sleek efficient design, uncomplicated.
Nice to have
• Sign up page vs just a contact page.
Should not have
• Lots of pages, hard to navigate,

```html
<!DOCTYPE html>
<html lang="en">
<head>
<meta charset="utf-8">
<title>Brimley &amp; Fox Care — Medical Consulting &amp; Brokerage</title>
<link rel="stylesheet" href="https://fonts.googleapis.com/css2?family=Inter:wght@400;500;600&display=swap">
<style>
  :root {
    --ink: #000000;
    --white: #ffffff;
    --sky: #7fd3f5;
    --sky-strong: #00a6e6;
    --navy: #0d5a96;
    --blue-deep: #0054aa;
    --blue-mid: #0677ba;
    --blue-soft: #7badd7;
    --tint: #eef7fc;
    --field-text: #8a8f96;
    --body-text: #1a1a1a;
  }
  * { box-sizing: border-box; margin: 0; padding: 0; }
  html, body { width: 1200px; height: 2754px; overflow: hidden; }
  body { position: relative; font-family: "Inter", Arial, sans-serif; color: var(--body-text); background: var(--white); }
  .abs { position: absolute; }

  /* header */
  .site-header { position: absolute; left: 0; top: 0; width: 1200px; height: 166px; background: var(--ink); }
  .brand { position: absolute; display: flex; align-items: center; gap: 10px; color: var(--white); font-weight: 600; font-size: 17px; }
  .brand-mark { width: 14px; height: 14px; background: var(--sky-strong); }
  .site-header .brand { left: 118px; top: 72px; }
  .nav { position: absolute; display: flex; color: var(--white); font-size: 17px; }
  .nav a { color: inherit; text-decoration: none; position: absolute; white-space: nowrap; }

  /* hero */
  .hero { position: absolute; left: 0; top: 166px; width: 1200px; height: 552px;
    background: linear-gradient(120deg, #0e4a52 0%, #2b3a3f 30%, #3c3f42 60%, #5a5d60 100%);
    clip-path: polygon(0 0, 100% 0, 100% 78%, 0 100%); }
  .hero-title { position: absolute; left: 110px; top: 262px; font-size: 58px; font-weight: 500; line-height: 66px; color: var(--white); letter-spacing: -0.5px; }
  .hero-title span { color: var(--sky); }
  .btn { position: absolute; display: flex; align-items: center; justify-content: center; font-size: 14px; font-weight: 500; text-transform: uppercase; }
  .btn-hero { left: 110px; top: 441px; width: 124px; height: 36px; background: var(--sky); color: var(--ink); }

  /* about */
  .about-photo { position: absolute; left: 120px; top: 776px; width: 438px; height: 438px; border-radius: 50%;
    border: 7px solid var(--blue-mid); background: radial-gradient(circle at 40% 40%, #e3f4ff 0%, #a9dcfb 55%, #5aa8e0 100%); }
  .about-title { position: absolute; left: 628px; top: 808px; width: 480px; font-size: 35px; line-height: 40px; font-weight: 400; color: var(--ink); }
  .about-text { position: absolute; left: 628px; top: 952px; width: 455px; font-size: 14px; line-height: 18.4px; }
  .btn-learn { left: 628px; top: 1148px; width: 124px; height: 36px; background: var(--sky); color: var(--white); }

  /* practice */
  .practice { position: absolute; left: 0; top: 1302px; width: 1200px; height: 926px;
    background: linear-gradient(180deg, var(--tint) 0%, #f6fbfe 40%, #ffffff 55%, #f2f5f6 70%, #dfe7ea 100%); }
  .practice-photo { position: absolute; left: 0; top: 1760px; width: 1200px; height: 468px;
    background: linear-gradient(180deg, rgba(255,255,255,0) 0%, #e8f3f4 35%, #cfe6ea 70%, #b9d2d6 100%); }
  .practice-title { position: absolute; left: 0; top: 1362px; width: 1170px; text-align: center; font-size: 34px; font-weight: 500; color: var(--ink); }
  .area { position: absolute; top: 1472px; width: 290px; }
  .area-icon { width: 66px; height: 66px; display: block; }
  .area h3 { margin-top: 28px; font-size: 28px; font-weight: 500; color: var(--ink); }
  .area p { margin-top: 14px; font-size: 14px; line-height: 20px; }
  .btn-view { left: 537px; top: 1813px; width: 124px; height: 36px; background: var(--sky); color: var(--white); }

  /* contact */
  .contact { position: absolute; left: 0; top: 2228px; width: 1200px; height: 379px;
    background: linear-gradient(180deg, var(--sky-strong) 0%, var(--blue-mid) 45%, var(--navy) 100%); }
  .contact-title { position: absolute; left: 103px; top: 2314px; font-size: 35px; font-weight: 500; color: var(--white); }
  .contact-text { position: absolute; left: 110px; top: 2374px; width: 370px; font-size: 14px; line-height: 20px; color: var(--white); }
  .field { position: absolute; background: var(--white); color: var(--field-text); font-size: 14px; padding: 12px 15px; }
  .btn-send { left: 560px; top: 2523px; width: 144px; height: 45px; background: var(--sky); color: var(--navy); text-transform: none; font-weight: 600; gap: 6px; }

  /* footer */
  .site-footer { position: absolute; left: 0; top: 2607px; width: 1200px; height: 147px; background: var(--ink); color: var(--white); }
  .site-footer .brand { left: 108px; top: 55px; font-size: 15px; }
  .contact-line { position: absolute; left: 308px; display: flex; align-items: center; gap: 10px; font-size: 14px; }
</style>
</head>
<body>

<header class="site-header">
  <div class="brand"><span class="brand-mark"></span>Brimley &amp; Fox Care</div>
  <nav class="nav">
    <a style="left:703px;top:76px">Home</a>
    <a style="left:789px;top:76px">About</a>
    <a style="left:870px;top:76px">Our Service</a>
    <a style="left:996px;top:76px">Contact Us</a>
  </nav>
</header>

<section class="hero" role="img" aria-label="Close-up photograph of dental handpiece instruments"></section>
<h1 class="hero-title">A Medical Consulting<br><span>&amp; Brokerage Firm</span></h1>
<a class="btn btn-hero">Contact Us</a>

<div class="about-photo" role="img" aria-label="Photograph of a bright dental treatment room in blue tones"></div>
<h2 class="about-title">Advocating for financial transparency in the medical supply world.</h2>
<p class="about-text">Lorem ipsum dolor sit amet consectetur. Turpis vitae aliquet sed odio. Adipiscing aliquam scelerisque eu lacus a. Et lobortis eleifend ullamcorper diam cursus est vel tellus. Diam auctor vitae eros tellus pharetra ut venenatis. Ut morbi dolor tincidunt pulvinar et maecenas ullamcorper quam. Lorem pulvinar velit elit vitae elit imperdiet. Tellus feugiat ornare feugiat magna vel. Sagittis eu dui et amet elit purus. Quis enim facilisi aliquet ipsum sit orci mattis scelerisque. Fringilla lorem sed risus duis dictum nibh nec.</p>
<a class="btn btn-learn">Learn More</a>

<section class="practice"></section>
<div class="practice-photo" role="img" aria-label="Photograph of a clean white dental clinic with a turquoise treatment chair"></div>
<h2 class="practice-title">Areas of Practice</h2>

<div class="area" style="left:110px">
  <svg class="area-icon" viewBox="0 0 66 66" aria-hidden="true">
    <rect width="66" height="66" fill="#000"/>
    <g stroke="#fff" stroke-width="2.5" fill="none">
      <circle cx="33" cy="33" r="6"/>
      <line x1="33" y1="27" x2="33" y2="16"/><line x1="33" y1="39" x2="33" y2="50"/>
      <line x1="27" y1="33" x2="16" y2="33"/><line x1="39" y1="33" x2="50" y2="33"/>
      <line x1="28" y1="28" x2="20" y2="20"/><line x1="38" y1="28" x2="46" y2="20"/>
      <line x1="28" y1="38" x2="20" y2="46"/><line x1="38" y1="38" x2="46" y2="46"/>
    </g>
  </svg>
  <h3>Distribution</h3>
  <p>Lorem ipsum dolor sit amet consectetur. Dictum urna gravida sed dolor egestas eget placerat molestie. Blandit nibh purus aliquam pellentesque. Fermentum malesuada massa urna enim. Sed tempor rhoncus volutpat elementum in orci elementum laoreet. Facilisi enim placerat nec placerat enim.</p>
</div>

<div class="area" style="left:449px">
  <svg class="area-icon" viewBox="0 0 66 66" aria-hidden="true">
    <rect width="66" height="66" fill="#00a6e6"/>
    <rect x="12" y="20" width="30" height="18" rx="9" transform="rotate(-40 27 29)" fill="#fff"/>
    <circle cx="43" cy="42" r="11" fill="#fff"/>
    <line x1="43" y1="31" x2="43" y2="53" stroke="#00a6e6" stroke-width="2.5"/>
  </svg>
  <h3>Pharma</h3>
  <p>Lorem ipsum dolor sit amet consectetur. Dictum urna gravida sed dolor egestas eget placerat molestie. Blandit nibh purus aliquam pellentesque. Fermentum malesuada massa urna enim. Sed tempor rhoncus volutpat elementum in orci elementum laoreet. Facilisi enim placerat nec placerat enim.</p>
</div>

<div class="area" style="left:808px">
  <svg class="area-icon" viewBox="0 0 66 66" aria-hidden="true">
    <rect width="66" height="66" fill="#000"/>
    <g stroke="#fff" stroke-width="2.5" fill="none" stroke-linecap="round">
      <path d="M16 22 L24 40 L44 40 L48 32"/>
      <line x1="34" y1="40" x2="34" y2="50"/><line x1="24" y1="50" x2="44" y2="50"/>
      <path d="M38 18 L46 14 L50 22"/>
    </g>
  </svg>
  <h3>Capital Equipment</h3>
  <p>Lorem ipsum dolor sit amet consectetur. Dictum urna gravida sed dolor egestas eget placerat molestie. Blandit nibh purus aliquam pellentesque. Fermentum malesuada massa urna enim. Sed tempor rhoncus volutpat elementum in orci elementum laoreet. Facilisi enim placerat nec placerat enim.</p>
</div>

<a class="btn btn-view">View All</a>

<section class="contact"></section>
<h2 class="contact-title">Get in Touch</h2>
<p class="contact-text">For all questions, inquires regarding our services, or assistance in referring someone to us. Please contact us below.</p>
<div class="field" style="left:562px;top:2293px;width:254px;height:40px">First Name</div>
<div class="field" style="left:832px;top:2293px;width:251px;height:40px">Last Name</div>
<div class="field" style="left:562px;top:2342px;width:254px;height:40px">Email Address</div>
<div class="field" style="left:832px;top:2342px;width:251px;height:40px">Phone number</div>
<div class="field" style="left:562px;top:2396px;width:521px;height:104px">Message</div>
<a class="btn btn-send">Send
  <svg width="12" height="12" viewBox="0 0 12 12" aria-hidden="true"><path d="M1 6h9M6.5 2.5 10 6l-3.5 3.5" stroke="#0d5a96" stroke-width="1.4" fill="none"/></svg>
</a>

<footer class="site-footer">
  <div class="brand"><span class="brand-mark"></span>Brimley &amp; Fox Care</div>
  <div class="contact-line" style="top:48px">
    <svg width="20" height="20" viewBox="0 0 24 24" aria-hidden="true"><path d="M5 3h4l2 5-2.5 1.5a11 11 0 0 0 6 6L16 13l5 2v4a2 2 0 0 1-2 2A16 16 0 0 1 3 5a2 2 0 0 1 2-2z" stroke="#fff" stroke-width="1.6" fill="none"/></svg>
    (555) 014-2290
  </div>
  <div class="contact-line" style="top:80px">
    <svg width="20" height="20" viewBox="0 0 24 24" aria-hidden="true"><rect x="3" y="5" width="18" height="14" rx="1.5" stroke="#fff" stroke-width="1.6" fill="none"/><path d="M3.5 6l8.5 7 8.5-7" stroke="#fff" stroke-width="1.6" fill="none"/></svg>
    info@brimleyandfoxcare.example
  </div>
  <nav class="nav">
    <a style="left:690px;top:50px">Home</a>
    <a style="left:776px;top:50px">About</a>
    <a style="left:857px;top:50px">Our Service</a>
    <a style="left:982px;top:50px">Contact Us</a>
  </nav>
</footer>

</body>
</html>
```